Need new, updated stationery design for an Orthodontic office - to include: Letterhead, Stationery C

Looking for something fresh and sophisticated. We need a stationery design for our new office that is similar to the files attached but do not want it to be exactly what we have now. Needs to include 3 offices - Addresses below:
Harrisburg Office
7315 Orchard Lane, Ste. 214
Harrisburg, NC 28075
Concord Office
2647 Pell-Rose Court NW, Ste. 500
Concord, NC 28025
Charlotte (Fernvale) Office
5913 Fernvale Corporate Parkway, Ste. 409
Charlotte, NC 28277
Phone Number is: 704-318-2967
Office Email: office@marcusweldtorth.example
Dr. Marcus Weldt
Website: www.marcusweldtorth.example
Office

```html
<!DOCTYPE html>
<html lang="en">
<head>
<meta charset="utf-8">
<title>Marcus Weldt Orthodontics — Stationery</title>
<link rel="stylesheet" href="https://fonts.googleapis.com/css2?family=Josefin+Sans:wght@400;600;700&display=swap">
<style>
  :root {
    --navy: #1d3c85;
    --ink: #2f3238;
    --decor: #d9dee7;
    --paper: #ffffff;
    --backdrop: #e6e6e8;
    --edge: rgba(0,0,0,0.08);
  }
  * { box-sizing: border-box; margin: 0; padding: 0; }
  html, body { width: 1200px; height: 801px; overflow: hidden; }
  body {
    background: var(--backdrop);
    font-family: "Josefin Sans", sans-serif;
    color: var(--ink);
    position: relative;
  }
  .sheet {
    position: absolute;
    background: var(--paper);
    box-shadow: 0 2px 6px var(--edge);
    overflow: hidden;
  }
  .decor-circle {
    position: absolute;
    border-radius: 50%;
    background: var(--decor);
  }
  .brand {
    display: flex;
    align-items: center;
    gap: 8px;
    color: var(--navy);
    font-weight: 700;
    text-transform: uppercase;
    letter-spacing: 0.06em;
    line-height: 1.1;
    white-space: nowrap;
  }
  .brand-name { display: block; }
  .brand-dot {
    flex: none;
    border-radius: 50%;
    background: var(--navy);
  }

  /* Envelope */
  .envelope { left: 20px; top: 30px; width: 540px; height: 235px; }
  .envelope .decor-circle { left: 40px; top: -70px; width: 220px; height: 220px; }
  .envelope .brand { position: absolute; right: 24px; bottom: 56px; font-size: 17px; }
  .envelope .brand-dot { width: 28px; height: 28px; }
  .envelope .office-line {
    position: absolute; right: 24px; bottom: 24px;
    color: var(--navy); font-weight: 600; font-size: 12px; letter-spacing: 0.02em;
    white-space: nowrap;
  }

  /* Business cards */
  .card { top: 310px; width: 260px; height: 149px; }
  .card-front { left: 20px; padding: 18px 16px; }
  .card-front .brand { font-size: 13px; }
  .card-front .brand-dot { width: 22px; height: 22px; }
  .card-offices {
    position: absolute; left: 14px; right: 14px; bottom: 16px;
    display: flex; justify-content: space-between; gap: 6px;
    font-size: 6px; line-height: 1.4; color: var(--navy);
    white-space: nowrap;
  }
  .card-offices strong { display: block; font-size: 7px; margin-bottom: 2px; }
  .card-back { left: 300px; }
  .card-back .decor-circle { left: 18px; top: 14px; width: 120px; height: 120px; }
  .card-person { position: absolute; right: 18px; top: 34px; text-align: right; }
  .card-person .name { font-weight: 700; font-size: 13px; color: var(--ink); }
  .card-person .role { font-size: 10px; margin-top: 3px; }
  .card-person .phone { font-weight: 600; font-size: 10px; margin-top: 10px; }
  .card-web {
    position: absolute; left: 14px; bottom: 14px;
    font-size: 7px; font-weight: 600; color: var(--ink);
    white-space: nowrap;
  }

  /* Letterhead */
  .letterhead { left: 590px; top: 20px; width: 588px; height: 761px; }
  .letterhead .decor-circle { left: 40px; top: 290px; width: 520px; height: 520px; }
  .letterhead .brand { position: absolute; left: 36px; top: 36px; font-size: 14px; }
  .letterhead .brand-dot { width: 26px; height: 26px; }
  .letter-offices {
    position: absolute; left: 220px; right: 30px; top: 34px;
    display: flex; justify-content: space-between; gap: 12px;
    font-size: 8.5px; line-height: 1.45; color: var(--navy); text-align: right;
    white-space: nowrap;
  }
  .letter-offices > div:nth-child(2) { margin-top: 22px; }
  .letter-offices > div:nth-child(3) { margin-top: 44px; }
  .letter-offices strong { display: block; font-size: 10px; margin-bottom: 2px; }
  .letter-body {
    position: absolute; left: 60px; right: 60px; top: 160px;
    font-size: 13px; line-height: 1.55; color: var(--ink);
  }
  .letter-body p { margin-bottom: 10px; }
  .letter-footer {
    position: absolute; left: 36px; bottom: 28px;
    color: var(--navy); font-weight: 600; font-size: 13px; letter-spacing: 0.03em;
    white-space: nowrap;
  }
</style>
</head>
<body>

  <section class="sheet envelope">
    <div class="decor-circle" role="img" aria-label="Large faint brand circle decoration"></div>
    <div class="brand"><span class="brand-dot"></span><span><span class="brand-name">Marcus Weldt</span><span class="brand-name">Orthodontics</span></span></div>
    <div class="office-line">Harrisburg • Concord • Charlotte (Fernvale)</div>
  </section>

  <section class="sheet card card-front">
    <div class="brand"><span class="brand-dot"></span><span><span class="brand-name">Marcus Weldt</span><span class="brand-name">Orthodontics</span></span></div>
    <div class="card-offices">
      <div><strong>Harrisburg</strong>7315 Orchard Lane,<br>Ste. 214, Harrisburg,<br>NC 28075</div>
      <div><strong>Concord</strong>2647 Pell-Rose Court NW,<br>Ste. 500, Concord,<br>NC 28025</div>
      <div><strong>Charlotte (Fernvale)</strong>5913 Fernvale Corporate<br>Parkway, Ste. 409,<br>Charlotte, NC 28277</div>
    </div>
  </section>

  <section class="sheet card card-back">
    <div class="decor-circle" role="img" aria-label="Faint brand circle decoration"></div>
    <div class="card-person">
      <div class="name">Dr. Marcus Weldt</div>
      <div class="role">Orthodontist</div>
      <div class="phone">T. 704-318-2967</div>
    </div>
    <div class="card-web">www.marcusweldtorth.example | office@marcusweldtorth.example</div>
  </section>

  <section class="sheet letterhead">
    <div class="decor-circle" role="img" aria-label="Large faint brand circle watermark"></div>
    <div class="brand"><span class="brand-dot"></span><span><span class="brand-name">Marcus Weldt</span><span class="brand-name">Orthodontics</span></span></div>
    <div class="letter-offices">
      <div><strong>Harrisburg</strong>7315 Orchard Lane,<br>Ste. 214, Harrisburg,<br>NC 28075</div>
      <div><strong>Concord</strong>2647 Pell-Rose Court NW,<br>Ste. 500, Concord,<br>NC 28025</div>
      <div><strong>Charlotte (Fernvale)</strong>5913 Fernvale Corporate Pkwy,<br>Ste. 409, Charlotte,<br>NC 28277</div>
    </div>
    <div class="letter-body">
      <p>Lorem Ipsum is simply dummy text of the printing and typesetting industry. Lorem Ipsum has been the industry's standard dummy text ever since the 1500s.</p>
      <p>Lorem Ipsum is simply dummy text of the printing and typesetting industry. Lorem Ipsum has been the industry's standard dummy text ever since the 1500s.</p>
      <p>Lorem Ipsum is simply dummy text of the printing and typesetting industry.</p>
      <p>Lorem Ipsum is simply dummy text of the printing and typesetting industry. Lorem Ipsum has been the industry's st</p>
    </div>
    <div class="letter-footer">PHONE - 704-318-2967 | EMAIL - office@marcusweldtorth.example</div>
  </section>

</body>
</html>
```